TotHaven Community Landing Page

TotHaven is a virtual world built with childrens' needs in mind. It is an online portal where parents will find all kids' related stuffs and a community connect point for parents to interact and share their experiences.

We need the designs for 2 pages within TotHaven:
- Landing Page for the Community Area
- Registration page for membership

1) The Landing Page need to have the following:

Logo & Main Background :- use the images attached

Page Title & Navigation Menu :-
The page title is "Community Connect"; navigation menu should be able to hold at least 6 tabs

Login Widget* :-
We want to put emphasis on the design of this.
For visitors, this is a normal login widget with username/password input fields, register button and 'login with chatterbook' button.
For logged-in users, this becomes a simple dashboard widget with Avatar, shortlinks and some useful navigation buttons.

"Groups" Section :-
This area holds an image, a short paragraph introducing "Groups", a widget showing 5-10 latest/popular groups and a 'Go to Groups' button at the bottom.

"Forum" Section :-
This area holds an image, a short paragraph introducing "Forum", a widget showing 5-10 latest/popular discussion topics and a 'Go to Forum' button at the bottom.

"Activities" Section -
This area holds an image, a short paragraph introducing "Forum", a widget showing 5-10 latest/popular events & activities and a 'Go to Activities' button at the bottom.

"Marketplace" Section :-
This area holds an image, a short paragraph introducing "Marketplace", a widget showing 5-10 latest/popular products and a 'Go to Marketplace' button at the bottom.

Social Media elements :-
The usual social media icons and chatterbook like box.

2) The Registration Page will need to contain the registration form as per the image attached.

Target Market(s)

Parents with kids ranging from 2 - 12 years old

Industry/Entity Type

Events

Requirements
Nice to have
• - colorful illustrations of kids or kids related images all around

```html
<!DOCTYPE html>
<html lang="en">
<head>
<meta charset="utf-8">
<title>TotHaven · Register</title>
<link rel="stylesheet" href="https://fonts.googleapis.com/css2?family=Fredoka+One&family=Sniglet:wght@800&family=Lato:ital,wght@0,700;1,400&family=Arimo:wght@400;700&family=Open+Sans:wght@700&display=swap">
<style>
  :root {
    --sky-top: #5fc3e4;
    --sky-mid: #2fa7dd;
    --sky-low: #9fdcf2;
    --hill-light: #8cbf2e;
    --hill-dark: #4d7a12;
    --white: #ffffff;
    --ink: #3b3b3b;
    --ink-soft: #555555;
    --ribbon: #a6d244;
    --ribbon-edge: #7fae25;
    --ribbon-tail: #8fc037;
    --cream: #fff3cf;
    --cream-edge: #f3dfa3;
    --yellow: #f7c908;
    --field: #fff3cf;
    --field-edge: #d6a90a;
    --orange: #f0960d;
    --note: #6b5200;
    --purple: #a51fe6;
    --purple-light: #c35cf7;
    --nav-red: #d3121b;
    --nav-orange: #f7801a;
    --nav-brown: #a23a3e;
    --nav-purple: #9b1fe0;
    --nav-blue: #33aee0;
    --nav-green: #49ab24;
    --social: #3b6bb5;
    --social-blue: #2b9ddd;
    --like: #3a5da8;
    --rule: #d9d9d9;
  }
  * { box-sizing: border-box; margin: 0; padding: 0; }
  html, body { width: 1200px; height: 1052px; overflow: hidden; }
  body { font-family: "Arimo", Arial, sans-serif; color: var(--ink); background: var(--white); }

  .canvas { position: relative; width: 1200px; height: 1052px; overflow: hidden; }

  .scene-sky {
    position: absolute; left: 0; top: 0; width: 1200px; height: 520px;
    background: linear-gradient(180deg, var(--sky-top) 0%, var(--sky-mid) 45%, var(--sky-low) 100%);
  }
  .scene-hills {
    position: absolute; left: 0; top: 420px; width: 1200px; height: 500px;
    background: linear-gradient(180deg, var(--hill-light) 0%, #6f9f1e 45%, var(--hill-dark) 100%);
  }
  .footer-ground { position: absolute; left: 0; top: 820px; width: 1200px; height: 232px; }

  .page-card {
    position: absolute; left: 166px; top: 36px; width: 863px; height: 756px;
    background: var(--white); border-radius: 8px;
    box-shadow: 0 2px 8px rgba(0,0,0,.18);
  }

  .brand { position: absolute; left: 198px; top: 78px; display: flex; align-items: center; gap: 10px; }
  .brand-dot { width: 30px; height: 30px; border-radius: 50%; background: var(--purple); }
  .brand-name { font-family: "Fredoka One", sans-serif; font-size: 44px; color: var(--purple); }

  .header-art {
    position: absolute; left: 537px; top: 58px; width: 300px; height: 119px;
    background: radial-gradient(ellipse at 50% 100%, #ffe2ea 0%, #fdeff4 45%, rgba(255,255,255,0) 75%);
  }

  .social { position: absolute; top: 111px; left: 812px; display: flex; gap: 6px; }
  .social-icon { width: 32px; height: 32px; border-radius: 50%; background: var(--social); }
  .social-icon.alt { background: var(--social-blue); }
  .like-button {
    position: absolute; left: 933px; top: 112px; width: 64px; height: 30px;
    background: var(--like); border-radius: 3px; color: var(--white);
    font: 700 12px/30px "Arimo", sans-serif; text-align: center;
  }

  .ribbon-tail { position: absolute; top: 203px; }
  .ribbon-tail.left { left: 84px; }
  .ribbon-tail.right { left: 1047px; }
  .ribbon {
    position: absolute; left: 147px; top: 177px; width: 903px; height: 67px;
    background: linear-gradient(180deg, #b7dc5a 0%, var(--ribbon) 60%, #93c534 100%);
    border-bottom: 3px solid var(--ribbon-edge);
  }
  .main-nav { position: absolute; top: 194px; left: 0; width: 1200px; height: 31px; }
  .nav-pill {
    position: absolute; height: 31px; border-radius: 16px;
    font: 15px/31px "Fredoka One", sans-serif; color: var(--white); text-align: center;
    box-shadow: inset 0 -3px 0 rgba(0,0,0,.15), inset 0 2px 0 rgba(255,255,255,.25);
    text-shadow: 0 1px 1px rgba(0,0,0,.3);
  }
  .nav-home { left: 211px; width: 98px; background: var(--nav-red); }
  .nav-market { left: 326px; width: 150px; background: var(--nav-orange); }
  .nav-activities { left: 495px; width: 125px; background: var(--nav-brown); }
  .nav-groups { left: 637px; width: 110px; background: var(--nav-purple); }
  .nav-forums { left: 764px; width: 112px; background: var(--nav-blue); }
  .nav-contact { left: 894px; width: 106px; background: var(--nav-green); }

  .page-title { position: absolute; left: 191px; top: 258px; font: 800 27px "Sniglet", sans-serif; color: var(--ink); }

  .signup-panel {
    position: absolute; left: 196px; top: 305px; width: 804px; height: 458px;
    background: var(--cream); border: 1px solid var(--cream-edge); border-radius: 10px;
  }
  .pencil-art {
    position: absolute; left: 942px; top: 284px; width: 44px; height: 72px;
    background: linear-gradient(160deg, #f6c11b 0%, #f3a91a 70%, #8b5a2b 100%);
    border-radius: 6px; transform: rotate(25deg);
  }
  .panel-title { position: absolute; left: 224px; top: 324px; font: 800 23px "Sniglet", sans-serif; color: var(--orange); }
  .panel-intro {
    position: absolute; left: 224px; top: 356px; width: 740px;
    font: 700 14px/19px "Arimo", sans-serif; color: var(--ink);
  }

  .form-box {
    position: absolute; left: 224px; top: 406px; width: 745px; height: 283px;
    background: var(--yellow); border-radius: 12px;
  }
  .form-heading {
    position: absolute; top: 422px; font: 800 22px "Sniglet", sans-serif; color: var(--white);
    text-shadow: 0 1px 1px rgba(0,0,0,.2);
  }
  .field {
    position: absolute; width: 329px; height: 38px; border-radius: 7px;
    background: var(--field); border: 1px solid var(--field-edge);
    box-shadow: inset 0 2px 2px rgba(0,0,0,.08);
    padding-left: 9px; font: 700 13px/37px "Lato", sans-serif; color: var(--ink);
  }
  .field em { font: italic 400 13px "Lato", sans-serif; color: #9a9079; }
  .field-note { position: absolute; left: 632px; top: 520px; font: 700 12px "Arimo", sans-serif; color: var(--note); }

  .submit-button {
    position: absolute; left: 260px; top: 705px; width: 680px; height: 41px; border-radius: 9px;
    background: linear-gradient(180deg, var(--purple-light) 0%, var(--purple) 60%, #8d12cc 100%);
    font: 700 21px/41px "Open Sans", sans-serif; color: var(--white); text-align: center;
  }

  .meadow-art {
    position: absolute; left: 750px; top: 810px; width: 118px; height: 67px; border-radius: 30px 30px 8px 8px;
    background: linear-gradient(180deg, #f7d7b5 0%, #e9a94f 100%);
  }
  .footer-art {
    position: absolute; left: 695px; top: 895px; width: 389px; height: 157px;
    background: radial-gradient(ellipse at 40% 100%, #ffe27a 0%, #fde6ef 40%, rgba(255,255,255,0) 72%);
  }

  .footer-brand { position: absolute; left: 160px; top: 940px; display: flex; align-items: center; gap: 8px; }
  .footer-brand .brand-dot { width: 24px; height: 24px; }
  .footer-brand .brand-name { font-size: 36px; }

  .footer-nav { position: absolute; top: 966px; left: 0; width: 1200px; font: 700 12.5px "Arimo", sans-serif; color: var(--ink); }
  .footer-nav span { position: absolute; }

  .footer-rule { position: absolute; left: 0; top: 1015px; width: 1200px; height: 1px; background: var(--rule); }
  .legal { position: absolute; top: 1025px; font: 13px "Arimo", sans-serif; color: var(--ink-soft); }
  .legal-link { text-decoration: underline; text-underline-offset: 3px; }
</style>
</head>
<body>
<div class="canvas">
  <div class="scene-sky" role="img" aria-label="Cartoon sky with a rainbow and soft clouds"></div>
  <div class="scene-hills" role="img" aria-label="Rolling green cartoon hills and bushes"></div>

  <svg class="footer-ground" width="1200" height="232" viewBox="0 0 1200 232" aria-hidden="true">
    <path d="M0 75 C120 40 220 110 340 80 C470 50 560 30 700 45 C820 55 960 20 1090 25 C1150 28 1180 40 1200 45 L1200 232 L0 232 Z" fill="var(--white)"/>
    <path d="M0 66 C120 31 220 101 340 71 C470 41 560 21 700 36 C820 46 960 11 1090 16 C1150 19 1180 31 1200 36" fill="none" stroke="#c7dd9a" stroke-width="2" stroke-dasharray="3 5"/>
  </svg>

  <div class="page-card"></div>

  <div class="brand">
    <span class="brand-dot"></span>
    <span class="brand-name">TotHaven</span>
  </div>
  <div class="header-art" role="img" aria-label="Two smiling cartoon children under a pastel rainbow with flowers"></div>

  <div class="social">
    <span class="social-icon" aria-label="chatterbook"></span>
    <span class="social-icon alt" aria-label="Short posts"></span>
    <span class="social-icon alt" aria-label="Professional network"></span>
  </div>
  <div class="like-button">Like</div>

  <svg class="ribbon-tail left" width="66" height="60" viewBox="0 0 66 60" aria-hidden="true">
    <polygon points="0,0 66,0 66,60 0,60 30,30" fill="var(--ribbon-tail)"/>
  </svg>
  <svg class="ribbon-tail right" width="66" height="60" viewBox="0 0 66 60" aria-hidden="true">
    <polygon points="0,0 66,0 36,30 66,60 0,60" fill="var(--ribbon-tail)"/>
  </svg>
  <div class="ribbon"></div>

  <nav class="main-nav">
    <span class="nav-pill nav-home">Home</span>
    <span class="nav-pill nav-market">Marketplace</span>
    <span class="nav-pill nav-activities">Activities</span>
    <span class="nav-pill nav-groups">Groups</span>
    <span class="nav-pill nav-forums">Forums</span>
    <span class="nav-pill nav-contact">Contact</span>
  </nav>

  <h1 class="page-title">Register:</h1>

  <section class="signup-panel"></section>
  <div class="pencil-art" role="img" aria-label="Cartoon yellow pencil"></div>
  <h2 class="panel-title">Create an Account:</h2>
  <p class="panel-intro">Registering for this site is easy, just fill in the fields below and we’ll get a new account set up for you in no time.</p>

  <div class="form-box"></div>
  <h3 class="form-heading" style="left:255px">Account Details</h3>
  <h3 class="form-heading" style="left:613px">Profile Details</h3>

  <div class="field" style="left:254px;top:475px">Username <em>(required)</em></div>
  <div class="field" style="left:254px;top:525px">Email Address <em>(required)</em></div>
  <div class="field" style="left:254px;top:576px">Choose a Password <em>(required)</em></div>
  <div class="field" style="left:254px;top:626px">Confirm Password <em>(required)</em></div>
  <div class="field" style="left:613px;top:475px">Name <em>(required)</em></div>
  <p class="field-note">This field can be seen by: Anyone</p>

  <div class="submit-button">Complete Sign up</div>

  <div class="meadow-art" role="img" aria-label="Cartoon child and kitten peeking over the hill"></div>
  <div class="footer-art" role="img" aria-label="Cartoon girl with a balloon beside a rainbow and sun"></div>

  <div class="footer-brand">
    <span class="brand-dot"></span>
    <span class="brand-name">TotHaven</span>
  </div>

  <nav class="footer-nav">
    <span style="left:531px">Home</span>
    <span style="left:589px">About us</span>
    <span style="left:666px">Groups</span>
    <span style="left:734px">Fourm</span>
    <span style="left:798px">Activities</span>
    <span style="left:877px">Marketplace</span>
  </nav>

  <div class="footer-rule"></div>
  <p class="legal" style="left:159px">TotHaven · Copyright 2013 · All rights reserved</p>
  <p class="legal legal-link" style="left:847px">Terms of service</p>
  <p class="legal legal-link" style="left:963px">Privacy policy</p>
</div>
</body>
</html>
```